Vibrant, yet professional, stationery set and other designs required.

I need to source a fantastic designer for a new project as part of my company using a new logo designed via pixel harbor.

**UPDATE** I am not looking for just 'fine' design that will suffice. I am looking for something great.

We are a life assurance brokerage based in Dublin, Ireland and HearthGuard.ie is our new website aimed at providing services for young families in Ireland. We are hoping to be the 'Vorn' level of service providers in this area and I am looking for the quality of design to reflect this :-) Hopefully that makes sense!

I have a preference for straight lines over curves and waves.

I need...

1. Business card
2. Letterhead
3. Banner (for printing - 76cm X 305cm)
4. Car branding for ZELKA 300 (2014 sport model) I believe the templates are freely available online.

Target Market(s)

Parents in Ireland - Aged 27 to 50.

Industry/Entity Type

Financial Planning

Colors

Designer to choose colors to be used in the design.

Requirements
Must have
• All of the items listed in the description above. I like clean, bright, legible, vibrant and professional design.
Should not have
• No silly or 'cheap' looking designs. This is a professional company looking to provide a professional service.

```html
<!DOCTYPE html>
<html lang="en">
<head>
<meta charset="utf-8">
<title>HearthGuard.ie – Business Card</title>
<link href="https://fonts.googleapis.com/css2?family=Open+Sans:wght@400;600;700&display=swap" rel="stylesheet">
<style>
  :root {
    --stage: #eceae6;
    --slate: #7b8d93;
    --slate-dark: #6a7b81;
    --paper: #f4f4f2;
    --white: #ffffff;
    --sky: #3bb7e0;
    --lime: #8cc21f;
    --tangerine: #f26b1d;
  }
  * { box-sizing: border-box; margin: 0; padding: 0; }
  html, body { width: 1200px; height: 800px; overflow: hidden; }
  body {
    background: var(--stage);
    font-family: "Open Sans", Arial, sans-serif;
    position: relative;
  }
  .card {
    position: absolute;
    top: 230px;
    width: 525px;
    height: 300px;
    border-radius: 4px;
    box-shadow: 0 6px 18px rgba(0,0,0,0.12);
    overflow: hidden;
  }
  .card--back { left: 50px; background: var(--slate); color: var(--white); }
  .card--front { left: 625px; background: var(--paper); }

  .wordmark {
    display: flex;
    align-items: center;
    gap: 10px;
    font-weight: 700;
    letter-spacing: -0.5px;
  }
  .wordmark__dot { border-radius: 50%; flex: none; }

  .card--back .wordmark { position: absolute; left: 34px; top: 40px; font-size: 34px; color: var(--white); }
  .card--back .wordmark__dot { width: 14px; height: 14px; background: var(--lime); }

  .identity { position: absolute; left: 34px; top: 102px; text-transform: uppercase; font-size: 14px; font-weight: 600; line-height: 1.3; }
  .identity__name { color: var(--sky); }
  .identity__role { color: var(--lime); }

  .address { position: absolute; left: 34px; top: 148px; font-size: 12.5px; line-height: 1.4; }

  .contacts { position: absolute; left: 34px; top: 192px; list-style: none; font-size: 12.5px; line-height: 1.45; }
  .contacts li { display: flex; align-items: center; gap: 8px; }
  .contacts svg { width: 11px; height: 11px; fill: var(--sky); flex: none; }

  .card--front .wordmark {
    position: absolute; left: 50%; top: 50%;
    transform: translate(-50%, -50%);
    font-size: 50px; color: var(--slate);
  }
  .card--front .wordmark__dot { width: 20px; height: 20px; background: var(--tangerine); }
</style>
</head>
<body>
  <section class="card card--back" aria-label="Business card, back">
    <div class="wordmark"><span>HearthGuard.ie</span><span class="wordmark__dot"></span></div>
    <div class="identity">
      <p class="identity__name">Aidan Kearney</p>
      <p class="identity__role">CEO/Founder</p>
    </div>
    <p class="address">42 Larkfield Row<br>Rathmines, Dublin D06 K2X4</p>
    <ul class="contacts">
      <li><svg viewBox="0 0 12 12"><path d="M1 3c0-1 1-2 2-2l1 2-1 1c1 2 2 3 4 4l1-1 2 1c0 1-1 2-2 2C4 10 1 7 1 3z"/></svg>014 963 2210</li>
      <li><svg viewBox="0 0 12 12"><path d="M3 0h6v12H3z M4 1v9h4V1z"/></svg>087 552 1840</li>
      <li><svg viewBox="0 0 12 12"><path d="M3 0h6v4H3z M1 4h10v6H1z"/></svg>014 963 2211</li>
      <li><svg viewBox="0 0 12 12"><path d="M0 2h12v8H0z M1 3l5 3 5-3z" fill-rule="evenodd"/></svg>aidan@hearthguard.ie</li>
      <li><svg viewBox="0 0 12 12"><circle cx="6" cy="6" r="5.5"/></svg>www.hearthguard.ie</li>
    </ul>
  </section>

  <section class="card card--front" aria-label="Business card, front">
    <div class="wordmark"><span>HearthGuard.ie</span><span class="wordmark__dot"></span></div>
  </section>
</body>
</html>
```